Product Label Design

Need a product design for our Epsom salt product, needs to have a luxurious simple feel to it. The picture attached is our brand and wordage on it, the bag we think should be a stand up bag that should be offwhite/creme color. The other picture are products that we like. We updated the packaging to be a Kraft tube box, please see the attached photo for dimensions.

```html
<!DOCTYPE html>
<html lang="en">
<head>
<meta charset="utf-8">
<title>Velmora Rise – Epsom Salt Pouch Front</title>
<link href="https://fonts.googleapis.com/css2?family=Montserrat:wght@600;700;800&display=swap" rel="stylesheet">
<style>
  :root {
    --backdrop: #b3b3b3;
    --pouch-light: #fbe3c0;
    --pouch-mid: #f3d3a8;
    --pouch-edge: #dcae78;
    --ink: #1c1a3a;
  }
  * { box-sizing: border-box; margin: 0; padding: 0; }
  html, body {
    width: 1200px;
    height: 928px;
    overflow: hidden;
    background: var(--backdrop);
    font-family: "Montserrat", sans-serif;
    color: var(--ink);
  }
  .canvas {
    position: relative;
    width: 1200px;
    height: 928px;
    display: flex;
    align-items: center;
    justify-content: center;
  }
  .pouch-front {
    position: relative;
    width: 570px;
    height: 880px;
    border-radius: 14px;
    background: radial-gradient(ellipse at 45% 45%, var(--pouch-light) 0%, var(--pouch-mid) 65%, var(--pouch-edge) 100%);
    text-align: center;
  }
  .zip-line {
    position: absolute;
    left: 28px;
    right: 28px;
    top: 66px;
    height: 4px;
    border-radius: 2px;
    background: var(--pouch-edge);
    opacity: 0.7;
  }
  .brand-name {
    position: absolute;
    top: 250px;
    left: 0;
    right: 0;
    font-weight: 700;
    font-size: 62px;
    letter-spacing: 1px;
    line-height: 1;
  }
  .scent-name {
    position: absolute;
    top: 384px;
    left: 0;
    right: 0;
    font-weight: 800;
    font-size: 48px;
    letter-spacing: 1px;
    line-height: 1;
  }
  .ingredients {
    position: absolute;
    top: 474px;
    left: 0;
    right: 0;
    font-weight: 700;
    font-size: 22px;
    line-height: 29px;
  }
  .net-weight {
    position: absolute;
    top: 806px;
    left: 0;
    right: 0;
    font-weight: 700;
    font-size: 19px;
    letter-spacing: 0.3px;
  }
</style>
</head>
<body>
  <main class="canvas">
    <section class="pouch-front">
      <div class="zip-line"></div>
      <h1 class="brand-name">Velmora</h1>
      <h2 class="scent-name">RISE</h2>
      <p class="ingredients">
        US Sourced Pure Epsom Salt<br>
        (Magnesium Sulfate)<br>
        + Abies sibirica<br>
        + Fir Balsam
      </p>
      <p class="net-weight">NET WT. SLBS (1360g)</p>
    </section>
  </main>
</body>
</html>
```